Surgical Procedure Room Letterhead

PLEASE DO NOT MAKE YOUR LETTERHEAD SIMILAR TO THE ONE I AM INCLUDING IN MY UPLOADS

Hello! I need my logo used to make a very clean, professional, simple letterhead that has all the pertinent information in it:
Location: 4182 NW 38th Lane, Suite 500
Tamarac, FL 33967
Phone: 954-218-4650
Fax: 800-642-9082

Can you please put this all on a word document that is easily editable? I will include my practice letterhead as an example ONLY of how easy it should be to write below the letterhead. Please don't make this letterhead the same as the one I am including in this example. They are two separate businesses.

Target Market(s)

Insurance companies

Industry/Entity Type

medical

Requirements
Must have
• classiness, elegance, simplicity
Should not have
• Please don't make your letterhead the same as the one that I included in my uploads

```html
<!DOCTYPE html>
<html lang="en">
<head>
<meta charset="utf-8">
<title>Halvern Suites Letterhead</title>
<link href="https://fonts.googleapis.com/css2?family=Arimo:wght@400&family=Mulish:wght@600;700;800&family=Open+Sans+Condensed:wght@300&display=swap" rel="stylesheet">
<style>
  :root {
    --backdrop: #cccccc;
    --paper: #ffffff;
    --navy: #0b2a55;
    --gold: #d4ae3a;
    --ink: #555555;
    --ink-dark: #4a4a4a;
  }
  * { margin: 0; padding: 0; box-sizing: border-box; }
  html, body {
    width: 1023px; height: 1200px; overflow: hidden;
    background: var(--backdrop);
  }
  .letterhead {
    position: absolute; left: 180px; top: 130px;
    width: 664px; height: 940px;
    background: var(--paper);
    color: var(--ink);
    font-family: "Arimo", Arial, sans-serif;
  }
  .brand {
    position: absolute; left: 62px; top: 54px;
    display: flex; align-items: center; gap: 10px;
  }
  .brand-dot {
    width: 30px; height: 30px; border-radius: 50%;
    border: 3px solid var(--gold);
  }
  .brand-name {
    font-family: "Mulish", sans-serif; font-weight: 800;
    font-size: 24px; letter-spacing: 1.5px; text-transform: uppercase;
    color: var(--navy); line-height: 1;
  }
  .salutation {
    position: absolute; left: 60px; top: 288px;
    font-family: "Mulish", sans-serif; font-weight: 700;
    font-size: 16px; color: var(--ink-dark);
  }
  .letter-body {
    position: absolute; left: 59px; top: 332px; width: 545px;
    font-size: 11.4px; line-height: 13.8px;
  }
  .letter-body p { margin-bottom: 12px; }
  .closing {
    position: absolute; left: 60px; top: 615px;
    font-family: "Mulish", sans-serif; font-weight: 700;
    font-size: 8.6px; color: var(--ink-dark);
  }
  .signature {
    position: absolute; left: 76px; top: 657px;
    font-family: "Open Sans Condensed", sans-serif; font-weight: 300;
    font-size: 17px; letter-spacing: -0.6px; color: var(--ink-dark);
  }
  .rule {
    position: absolute; top: 879px; height: 4px;
  }
  .rule-navy { left: 56px; width: 275px; background: var(--navy); }
  .rule-gold { left: 333px; width: 275px; background: var(--gold); }
  .contact {
    position: absolute; left: 56px; top: 898px; width: 552px;
    display: flex; justify-content: space-between; align-items: center;
    font-size: 11px; color: var(--ink);
  }
  .contact-item { display: flex; align-items: center; gap: 5px; }
  .contact-icon { width: 8px; height: 8px; fill: var(--gold); }
  .divider { color: var(--ink-dark); font-size: 13px; }
</style>
</head>
<body>
  <main class="letterhead">
    <header class="brand">
      <span class="brand-dot"></span>
      <span class="brand-name">Halvern Suites</span>
    </header>

    <h1 class="salutation">Dear Mr. Holt,</h1>

    <section class="letter-body">
      <p>Lorem ipsum dolor sit amet, consectetuer adipiscing elit, sed diam nonmmy nibh euismod tincidunt ut laor eet dolore magna aliquam erat volutpat. Ut wisi enim ad minim veniam, quis nostrud exerci tationmcorper suscipit lobortis nisl ut aliquip ex ea commodo consequat. Duis autem vel eum iriure dolor in hendrerit in vulputate velit esse molestie consequat, vel illum dolore eu feugiat</p>
      <p>Rorem ipsum dolor sit amet, consectetuer adipiscing elit, sed diam nonmmy nibh euismod tincidunt ut laor eet dolore magna aliquam erat volutpat. Ut wisi enim ad minim veniam, quis nostrud exerci tationmcorper suscipit lobortis nisl ut aliquip ex ea commodo consequat. Duis autem vel eum iriure dolor in hendrerit in vulputate velit esse molest</p>
      <p>Dorem ipsum dolor sit amet, consectetuer adipiscing elit, sed diam nonmmy nibh euismod tincidunt ut laor eet dolore magna aliquam erat volutpat. Ut wisi enim ad minim veniam, quis nostrud exerci tationmcorper suscipit lobortis nisl ut aliquip ex ea commodo consequat. Duis autem vel eum iriure dolor in hendrerit in suscipit lobortis nisl ut aliquip ex ea commodo consequat. Duis autem vel eum iriure dolor in hendrerit in vulputate velit esse molestie consequat, vel illum</p>
      <p>Sorem ipsum dolor sit amet, consectetuer adipiscing elit, sed diam nonmmy nibh euismod tincidunt ut laor eet dolore magna aliquam erat volutpat. Ut wisi enim ad minim veniam, quis nostrud exerci tationmcorper suscipit lobortis nisl ut aliquip ex ea commodo consequat. Duis autem vel eum iriure dolor in</p>
    </section>

    <p class="closing">Sincerely,</p>
    <p class="signature">Marcel Avery</p>

    <div class="rule rule-navy"></div>
    <div class="rule rule-gold"></div>

    <footer class="contact">
      <span class="contact-item">
        <svg class="contact-icon" viewBox="0 0 24 24" aria-hidden="true"><path d="M6.6 10.8a15.1 15.1 0 0 0 6.6 6.6l2.2-2.2a1 1 0 0 1 1-.25 11.4 11.4 0 0 0 3.6.57 1 1 0 0 1 1 1V20a1 1 0 0 1-1 1A17 17 0 0 1 3 4a1 1 0 0 1 1-1h3.5a1 1 0 0 1 1 1c0 1.25.2 2.45.57 3.57a1 1 0 0 1-.25 1z"/></svg>
        954-218-4650
      </span>
      <span class="divider">|</span>
      <span class="contact-item">
        <svg class="contact-icon" viewBox="0 0 24 24" aria-hidden="true"><path d="M6 2h10l2 2v5H6zM3 10h18a1 1 0 0 1 1 1v8a1 1 0 0 1-1 1H3a1 1 0 0 1-1-1v-8a1 1 0 0 1 1-1zm4 3v2h4v-2zm7 0v2h3v-2z"/></svg>
        800-642-9082
      </span>
      <span class="divider">|</span>
      <span class="contact-item">4182 NW 38th Lane, Suite 500, Tamarac, FL 33967</span>
    </footer>
  </main>
</body>
</html>
```